8"x5" postcard for Wireless Internet introduction to new mountain town market

I need to market high speed internet to a resort mountain town without doing the obvious laptop on a mountain top thing, so tired. We are going to be competing directly with another provider with same cost, but we will be offering free installation. The area is Aspen Colorado, so the clientele are outdoor types who have suffered for years from being disconnected in their mountain town. We offer fast internet and excellent customer service from people who live in their neck of the woods.

Target Market(s)

23-55 years old, both resort living, families and ski bums

Font styles to use
Sans Serif

Colors

Designer to choose colors to be used in the design.

Requirements
Must have
• Visual appeal and fresh verbiage. We don't mind being a little edgy. We are a young company and we want to appeal to people looking for a provider who gets them. We prefer a clean look.
Nice to have
• Nice to have colors that match our logo
Should not have
• stuffy concepts or verbiage that is too much like a car salesman. We don't want to look like a 'big box' company.

```html
<!DOCTYPE html>
<html lang="en">
<head>
<meta charset="utf-8">
<title>Ridgeway Broadband Postcard</title>
<link rel="stylesheet" href="https://fonts.googleapis.com/css2?family=Montserrat:wght@400;700;800;900&display=swap">
<style>
  :root {
    --ink: #0a0a0a;
    --panel: #f4f5f7;
    --gold: #f6c31c;
    --amber: #f8ae3c;
    --lemon: #f6de1e;
    --white: #ffffff;
    --brand-text: #2a2a2a;
  }
  * { margin: 0; padding: 0; box-sizing: border-box; }
  html, body { width: 1093px; height: 1200px; overflow: hidden; background: #ffffff; }
  body { position: relative; font-family: "Montserrat", sans-serif; }

  .postcard {
    position: absolute;
    left: 172px; top: 0;
    width: 821px; height: 1317px;
    transform: scale(0.91116);
    transform-origin: top left;
    background: var(--ink);
    overflow: hidden;
  }
  .postcard-shapes { position: absolute; inset: 0; }

  .headline {
    position: absolute; left: 0; right: 0; top: 160px;
    text-align: center; color: var(--white);
    font-weight: 900; font-size: 74px; line-height: 92px; letter-spacing: -1px;
  }

  .feature {
    position: absolute; top: 666px;
    color: var(--gold); font-weight: 900; font-size: 36px; line-height: 38px;
  }
  .feature--install { left: 107px; }
  .feature--support { left: 529px; }

  .price-tab {
    position: absolute; left: 43px; top: 848px;
    font-weight: 900; font-size: 22px; color: var(--ink);
  }

  .speed {
    position: absolute; top: 900px; text-align: left; color: var(--ink);
  }
  .speed-value { display: block; font-weight: 900; font-size: 120px; line-height: 124px; letter-spacing: -4px; }
  .speed-unit { display: block; font-weight: 700; font-size: 22px; line-height: 22px; margin-top: -14px; }
  .speed--10 { left: 88px; }
  .speed--10 .speed-unit { padding-left: 14px; }
  .speed--25 { left: 336px; }
  .speed--25 .speed-unit { padding-left: 4px; }
  .speed--40 { left: 576px; }
  .speed--40 .speed-unit { padding-left: 4px; }

  .brand {
    position: absolute; left: 118px; top: 1110px;
    color: var(--brand-text); font-weight: 800; font-size: 30px; line-height: 32px; letter-spacing: 1px;
  }

  .call {
    position: absolute; left: 447px; width: 374px; top: 1078px; text-align: center; color: var(--ink);
  }
  .call-title { display: block; font-weight: 900; font-size: 42px; line-height: 48px; }
  .call-phone { display: block; font-weight: 900; font-size: 32px; line-height: 40px; }

  .site {
    position: absolute; left: 0; right: 0; top: 1250px; text-align: center;
    color: var(--white); font-weight: 400; font-size: 21px; letter-spacing: 0.5px;
  }
  .site-url { color: var(--gold); font-weight: 800; }
</style>
</head>
<body>
  <main class="postcard">
    <svg class="postcard-shapes" viewBox="0 0 821 1317" width="821" height="1317">
      <defs>
        <radialGradient id="fiberGlow" cx="50%" cy="20%" r="80%">
          <stop offset="0" stop-color="#8a6320"/>
          <stop offset="0.45" stop-color="#4a3210"/>
          <stop offset="1" stop-color="#120d07"/>
        </radialGradient>
        <linearGradient id="ctaFill" x1="0" y1="0" x2="1" y2="0">
          <stop offset="0" stop-color="#f8ae3c"/>
          <stop offset="1" stop-color="#f6de1e"/>
        </linearGradient>
        <linearGradient id="bandFill" x1="0" y1="0" x2="1" y2="0">
          <stop offset="0" stop-color="#f6de1e"/>
          <stop offset="1" stop-color="#f6c31c"/>
        </linearGradient>
      </defs>

      <rect class="hero-photo" x="0" y="0" width="821" height="660" fill="url(#fiberGlow)"
            role="img" aria-label="Glowing amber fibre optic strands against a dark background"/>

      <polygon class="swoosh-shadow" points="0,452 227,560 0,520" fill="#111"/>
      <polygon class="swoosh-amber" points="0,508 227,560 821,515 0,650" fill="#f8ae3c"/>
      <polygon class="swoosh-yellow" points="0,582 821,515 0,614" fill="url(#bandFill)"/>
      <polygon class="lower-field" points="0,650 821,515 821,1317 0,1317" fill="#0a0a0a"/>

      <g class="feature-divider">
        <line x1="463" y1="676" x2="463" y2="774" stroke="#f6c31c" stroke-width="3"/>
        <circle cx="463" cy="725" r="9" fill="#f6c31c"/>
      </g>

      <rect class="speed-panel" x="0" y="861" width="821" height="195" fill="#f4f5f7"/>
      <polygon class="price-tab-shape" points="0,832 392,832 415,858 392,885 0,885" fill="url(#bandFill)"/>

      <g class="speed-divider" fill="#0a0a0a" stroke="#0a0a0a">
        <line x1="282" y1="934" x2="282" y2="1016" stroke-width="2"/>
        <circle cx="282" cy="976" r="5"/>
        <line x1="528" y1="934" x2="528" y2="1016" stroke-width="2"/>
        <circle cx="528" cy="976" r="5"/>
      </g>

      <rect class="contact-panel" x="0" y="1083" width="821" height="126" fill="#f4f5f7"/>
      <polygon class="cta-shape" points="447,1058 821,1058 821,1209 447,1209 387,1133" fill="url(#ctaFill)"/>
      <circle class="brand-dot" cx="76" cy="1141" r="30" fill="#f6c31c"/>
    </svg>

    <h1 class="headline">BETTER,<br>NOT BIGGER!</h1>

    <p class="feature feature--install">FREE<br>RESIDENTIAL<br>INSTALLATION</p>
    <p class="feature feature--support">IN-HOUSE<br>TECH<br>SUPPORT</p>

    <p class="price-tab">PRICES START AT $59.95</p>

    <div class="speed speed--10"><span class="speed-value">10</span><span class="speed-unit">mbps</span></div>
    <div class="speed speed--25"><span class="speed-value">25</span><span class="speed-unit">mbps</span></div>
    <div class="speed speed--40"><span class="speed-value">40</span><span class="speed-unit">mbps</span></div>

    <p class="brand">RIDGEWAY<br>BROADBAND</p>

    <p class="call"><span class="call-title">CALL NOW!</span><span class="call-phone">1 888 555 0142</span></p>

    <p class="site">VISIT US ONLINE AT <span class="site-url">WWW.RIDGEWAYBB.COM/ASPEN</span></p>
  </main>
</body>
</html>
```